Building Servicess

We need a new business card design for a company. We specialise in: Electrical/Site temporary electrics, Data/Network Installation, Passive Fire Protection

Industry/Entity Type

Construction

Contact Information for Business Card

Services provided as detailed on project description

Font styles to use
Serif

Colors
0054AA
0677BA
7BADD7
CADEEF
E8F1F8
00AB8E
00BBA5
67D7C9
C6EFE9
E9F9F6
EB3D1F
EC4F4E
F09395
F8D3D4
FCEDEE

Requirements
Must have
• Company logo-contact details-phone numbers

```html
<!DOCTYPE html>
<html lang="en">
<head>
<meta charset="utf-8">
<title>Business Card – Norvale Solution Services Ltd</title>
<link href="https://fonts.googleapis.com/css2?family=Lora:wght@700&family=Lato:wght@400&display=swap" rel="stylesheet">
<style>
  :root {
    --stage: #b3b3b3;
    --card-front: #ffffff;
    --card-back: #5a5a5c;
    --pattern-light: #76777a;
    --pattern-dark: #6a6b6e;
    --brand-blue: #1a78c2;
    --brand-grey: #808184;
    --ink: #222222;
    --ink-soft: #333333;
  }
  html, body {
    margin: 0;
    padding: 0;
    width: 1200px;
    height: 1200px;
    overflow: hidden;
    background: var(--stage);
  }
  .canvas {
    position: relative;
    width: 1200px;
    height: 1200px;
  }
  .card {
    position: absolute;
    top: 205px;
    width: 451px;
    height: 789px;
  }
  .card-front {
    left: 103px;
    background: var(--card-front);
  }
  .card-back {
    left: 645px;
    height: 790px;
    background: var(--card-back);
  }

  /* Company name block */
  .company {
    position: absolute;
    top: 88px;
    left: 0;
    width: 100%;
    text-align: center;
    font-family: "Lora", serif;
    font-weight: 700;
    color: var(--brand-blue);
  }
  .company-square {
    display: block;
    width: 56px;
    height: 56px;
    margin: 0 auto 14px;
    background: var(--brand-blue);
  }
  .company-name {
    margin: 0;
    font-size: 40px;
    line-height: 1.05;
    letter-spacing: 1px;
  }
  .company-sub {
    margin: 4px 0 0;
    font-size: 21px;
    line-height: 1.2;
    letter-spacing: 1px;
  }

  /* Person */
  .person {
    position: absolute;
    top: 394px;
    left: 0;
    width: 100%;
    text-align: center;
  }
  .person-name {
    margin: 0;
    font-family: "Lora", serif;
    font-weight: 700;
    font-size: 32px;
    line-height: 1;
  }
  .person-name .first { color: var(--brand-blue); }
  .person-name .last { color: var(--brand-grey); }
  .person-role {
    margin: 7px 0 0;
    font-family: "Lato", sans-serif;
    font-size: 18px;
    letter-spacing: 0.3px;
    color: var(--ink-soft);
  }

  /* Contact icons */
  .contact-icons {
    position: absolute;
    top: 492px;
    left: 0;
    width: 100%;
    display: flex;
    justify-content: center;
    gap: 8px;
  }
  .contact-icons svg {
    width: 20px;
    height: 20px;
  }

  /* Contact details */
  .contact-list {
    position: absolute;
    top: 551px;
    left: 0;
    width: 100%;
    margin: 0;
    padding: 0;
    list-style: none;
    text-align: center;
    font-family: "Lato", sans-serif;
    font-size: 18px;
    color: var(--ink);
  }
  .contact-list li { height: 34px; line-height: 30px; }
  .contact-list li.gap { margin-top: 3px; }

  /* Back */
  .back-pattern {
    position: absolute;
    left: 30px;
    top: 50px;
    width: 392px;
    height: 706px;
    background: linear-gradient(180deg, var(--pattern-light), var(--pattern-dark));
  }
  .back-brand {
    position: absolute;
    right: 29px;
    bottom: 34px;
    display: flex;
    align-items: center;
    gap: 10px;
    padding: 10px 0 10px 14px;
    background: var(--card-back);
  }
  .back-brand-name {
    margin: 0;
    font-family: "Lora", serif;
    font-weight: 700;
    font-size: 22px;
    letter-spacing: 1px;
    color: var(--brand-blue);
  }
  .back-brand-square {
    display: block;
    width: 53px;
    height: 53px;
    background: var(--brand-blue);
  }
</style>
</head>
<body>
<main class="canvas">

  <section class="card card-front" aria-label="Business card front">
    <header class="company">
      <span class="company-square" aria-hidden="true"></span>
      <p class="company-name">NORVALE</p>
      <p class="company-sub">SOLUTION SERVICES LTD</p>
    </header>

    <div class="person">
      <h1 class="person-name"><span class="first">Marek</span> <span class="last">Olszewski</span></h1>
      <p class="person-role">MANAGING DIRECTOR</p>
    </div>

    <div class="contact-icons" aria-hidden="true">
      <svg viewBox="0 0 20 20"><circle cx="10" cy="10" r="10" fill="var(--brand-blue)"/><path d="M4 8.5 Q10 4 16 8.5 L15 10 L12.5 9 L12.5 8 Q10 7 7.5 8 L7.5 9 L5 10 Z" fill="#fff"/><rect x="6" y="10.5" width="8" height="5" rx="1" fill="#fff"/></svg>
      <svg viewBox="0 0 20 20"><circle cx="10" cy="10" r="10" fill="var(--brand-blue)"/><path d="M6 5 L8 5 L9 8 L7.8 9 Q9 11.5 11 12.2 L12 11 L15 12 L15 14 Q14 15.5 12 15 Q6.5 13 5 8 Q4.6 6 6 5 Z" fill="#fff"/></svg>
      <svg viewBox="0 0 20 20"><circle cx="10" cy="10" r="10" fill="var(--brand-blue)"/><path d="M4.5 9.5 L15.5 5 L12.5 15 L9.5 11 Z" fill="#fff"/><path d="M9.5 11 L15.5 5" stroke="var(--brand-blue)" stroke-width="0.9"/></svg>
      <svg viewBox="0 0 20 20"><circle cx="10" cy="10" r="10" fill="var(--brand-blue)"/><g fill="none" stroke="#fff" stroke-width="1.6" stroke-linecap="round"><path d="M9 8.5 L11.2 6.3 A2 2 0 0 1 14 9.1 L12.5 10.6"/><path d="M11 11.5 L8.8 13.7 A2 2 0 0 1 6 10.9 L7.5 9.4"/><path d="M8.5 11.5 L11.5 8.5"/></g></svg>
    </div>

    <ul class="contact-list">
      <li>020 40987613</li>
      <li>075 18394725</li>
      <li class="gap">marekolszewski@mailbox.com</li>
      <li>www.marekolszewski.com</li>
    </ul>
  </section>

  <section class="card card-back" aria-label="Business card back">
    <div class="back-pattern" role="img" aria-label="Repeating grid of the company monogram in grey"></div>
    <div class="back-brand">
      <p class="back-brand-name">NORVALE</p>
      <span class="back-brand-square" aria-hidden="true"></span>
    </div>
  </section>

</main>
</body>
</html>
```